Vision Board Class Design needed

Hello, I need a business card design for a new Company based in Mount Waverley, Victoria, Australia. The Company provides a training Class with approx. 5 guests. They learn how to choose and create positive things in their life. It is based on the principal of the Law of Attraction. Each guest receives a large coloured cardboard and magazines, affirmations to choose ideas to help create their new exciting life - all pasted onto a "Vision Board" which will be seen by them every day and help to clarify the vision and attract abundance, happiness & positivity into their lives. I would like to see designs with bright, happy colours - perhaps rainbows - anything that represents a new life and appears refreshing.
Many thanks.

Industry/Entity Type

Training

Contact Information for Business Card

Dream Harbour
Lorna
Mobile 0473 259-386

Logo Text

Dream Harbour

Logo styles of interest
Abstract Logo
Requirements
Must have
• Happy, Bright colours!

```html
<!DOCTYPE html>
<html lang="en">
<head>
<meta charset="utf-8">
<title>Dream Harbour – Business Card</title>
<link rel="stylesheet" href="https://fonts.googleapis.com/css2?family=Great+Vibes&family=Cormorant+Garamond:ital,wght@1,500&display=swap">
<style>
  :root {
    --backdrop: #2a2a2a;
    --card-white: #ffffff;
    --card-grey: #e4e4e4;
    --ink: #111111;
    --ink-soft: #222222;
    --title-light: #f6f6f6;
    --tone-warm: #e38a2a;
    --tone-rose: #c24a9a;
    --tone-blue: #3f64c4;
    --tone-aqua: #3fb0c8;
    --tone-green: #5bb84a;
  }
  * { margin: 0; padding: 0; box-sizing: border-box; }
  html, body {
    width: 1200px;
    height: 900px;
    overflow: hidden;
    background: var(--backdrop);
  }
  .stage {
    width: 1200px;
    height: 900px;
    display: flex;
    align-items: center;
    justify-content: center;
    gap: 40px;
  }
  .card {
    position: relative;
    width: 540px;
    height: 310px;
    overflow: hidden;
    box-shadow: 0 14px 30px rgba(0, 0, 0, 0.55);
  }
  /* Front side: soft colour field with the company name */
  .card-front .colour-field {
    position: absolute;
    inset: 0;
    background: linear-gradient(100deg,
      var(--tone-warm) 0%,
      var(--tone-rose) 25%,
      var(--tone-blue) 45%,
      var(--tone-aqua) 62%,
      var(--tone-green) 80%,
      var(--tone-warm) 100%);
  }
  .card-front .front-title {
    position: absolute;
    inset: 0;
    display: flex;
    align-items: center;
    justify-content: center;
    font-family: "Great Vibes", cursive;
    font-weight: 400;
    font-size: 70px;
    color: var(--title-light);
    white-space: nowrap;
  }
  /* Back side: contact details */
  .card-back {
    background: linear-gradient(160deg, var(--card-white) 0%, var(--card-white) 45%, var(--card-grey) 100%);
    display: flex;
    flex-direction: column;
    align-items: center;
    color: var(--ink);
  }
  .card-back .brand-name {
    margin-top: 62px;
    font-family: "Great Vibes", cursive;
    font-size: 44px;
    line-height: 1;
    color: var(--ink);
  }
  .card-back .person-name {
    margin-top: 34px;
    font-family: "Great Vibes", cursive;
    font-weight: 400;
    font-size: 64px;
    line-height: 1;
    color: var(--ink);
  }
  .card-back .phone {
    margin-top: 12px;
    font-family: "Cormorant Garamond", serif;
    font-style: italic;
    font-weight: 500;
    font-size: 26px;
    letter-spacing: 2px;
    color: var(--ink-soft);
  }
</style>
</head>
<body>
<main class="stage">
  <section class="card card-front" aria-label="Business card front">
    <div class="colour-field" role="img" aria-label="Decorative bright rainbow colour pattern"></div>
    <h1 class="front-title">Dream Harbour</h1>
  </section>

  <section class="card card-back" aria-label="Business card back">
    <p class="brand-name">Dream Harbour</p>
    <h2 class="person-name">Lorna</h2>
    <p class="phone">0473 259-386</p>
  </section>
</main>
</body>
</html>
```